Established food business needs a new name card design

Refer to attached current name card. Would like a new professional look design with only the company name and logo without any pictures. Would like green and yellow to be included.
To include:
My name "IBRAHIM SUKRI" and hand phone number "87260413".
To delete "
"Along Brackendale Ave 8" and
"www.nur-tiwas.com.sg"
To change email to:
"tkr27@velmorix.com.sg"

```html
<!DOCTYPE html>
<html lang="en">
<head>
<meta charset="utf-8">
<title>NUR-TIWAS Name Card</title>
<link href="https://fonts.googleapis.com/css2?family=Lato:wght@400;700;900&display=swap" rel="stylesheet">
<style>
  :root {
    --green-light: #0c5e3c;
    --green-deep: #053a25;
    --gold: #f0c419;
    --gold-deep: #d2ac0c;
    --paper: #ffffff;
    --ink-light: #e4ebe7;
    --backdrop: #eceae6;
  }
  * { margin: 0; padding: 0; box-sizing: border-box; }
  html, body { width: 1200px; height: 900px; overflow: hidden; }
  body {
    background: var(--backdrop);
    font-family: "Lato", sans-serif;
    position: relative;
  }
  .card {
    position: absolute;
    left: 300px;
    width: 600px;
    height: 343px;
    overflow: hidden;
    background: radial-gradient(ellipse at 50% 40%, var(--green-light) 0%, var(--green-deep) 85%);
    box-shadow: 0 6px 18px rgba(0,0,0,0.18);
  }
  .card--front { top: 80px; }
  .card--back { top: 477px; }

  .brand {
    position: absolute;
    display: flex;
    align-items: center;
    gap: 12px;
  }
  .brand__circle {
    width: 44px; height: 44px;
    border-radius: 50%;
    border: 4px solid var(--gold);
  }
  .brand__name {
    color: var(--gold);
    font-weight: 900;
    font-size: 34px;
    letter-spacing: 1px;
    line-height: 1;
  }
  .card--front .brand { left: 50%; top: 50%; transform: translate(-50%, -50%); }
  .card--back .brand { left: 322px; top: 56px; }
  .card--back .brand__circle { width: 40px; height: 40px; }
  .card--back .brand__name { font-size: 30px; }

  .wave { position: absolute; left: 0; top: 0; width: 600px; height: 343px; }

  .holder { position: absolute; left: 44px; top: 54px; }
  .holder__name {
    color: var(--gold);
    font-weight: 900;
    font-size: 22px;
    letter-spacing: 2px;
  }
  .holder__cell {
    color: var(--gold);
    font-size: 16px;
    margin-top: 2px;
    margin-left: 4px;
  }

  .contact {
    position: absolute;
    left: 72px;
    top: 150px;
    color: var(--ink-light);
    font-size: 16px;
    line-height: 1.3;
  }
  .contact__line { display: flex; align-items: center; gap: 4px; }
  .contact__icon { width: 16px; height: 14px; flex: none; }
  .contact__address { margin-top: 10px; margin-left: 24px; }
</style>
</head>
<body>

<section class="card card--front">
  <div class="brand">
    <span class="brand__circle"></span>
    <span class="brand__name">NUR-TIWAS</span>
  </div>
</section>

<section class="card card--back">
  <svg class="wave" viewBox="0 0 600 343" aria-hidden="true">
    <path d="M0,280 C190,278 370,236 480,168 C380,250 200,304 0,308 Z" fill="var(--gold-deep)"/>
    <path d="M0,300 C170,298 340,262 440,205 C510,165 560,150 600,148 L600,343 L0,343 Z" fill="var(--paper)"/>
  </svg>

  <div class="holder">
    <div class="holder__name">IBRAHIM SUKRI</div>
    <div class="holder__cell">Cell : 87260413</div>
  </div>

  <div class="brand">
    <span class="brand__circle"></span>
    <span class="brand__name">NUR-TIWAS</span>
  </div>

  <div class="contact">
    <div class="contact__line">
      <svg class="contact__icon" viewBox="0 0 16 14" aria-hidden="true">
        <path d="M1,4 C1,1 15,1 15,4 L12,5 L11,3.5 L5,3.5 L4,5 Z" fill="var(--gold)"/>
        <rect x="3" y="6" width="10" height="7" rx="1" fill="var(--gold)"/>
      </svg>
      <span>65182937</span>
    </div>
    <div class="contact__line">
      <svg class="contact__icon" viewBox="0 0 16 14" aria-hidden="true">
        <rect x="1" y="2" width="14" height="10" fill="var(--gold)"/>
        <path d="M1,2 L8,8 L15,2" fill="none" stroke="var(--green-deep)" stroke-width="1.3"/>
      </svg>
      <span>tkr27@velmorix.com.sg</span>
    </div>
    <div class="contact__address">
      12 Kelvara Industrial<br>
      Estate Road 2# 02-08<br>
      Singapore 738104
    </div>
  </div>
</section>

</body>
</html>
```